Corporate brochure for a multinational construction company

Designing the cover pages and inside pages layout for a construction company which has operations in GCC, India etc. It has to be a very classy design. you can visit our website www.belvorant.com for more details on the company. Specific information required for the brochure design will be uploaded as needed.

Please note
1. Though the brochure will be around 80 pages, we need design of only the following
a. Cover page
b. CEOs message page
c. Introduction to sectors (Civil, Electrical, Mechanical, Infra)
d. Pages showing engineering expertise
e. Pages showing Project highlights (buildings etc)
f. Gallery pages (2 to 4 images in each page showing completed projects with a small text)
g. Key personnel (images and positions of key staff)

So design has to be done for a maximum of 7 to 10 pages. rest will be repetition.
Please use stock images with the above tip and send your designs.
g.
Updates

Project Deadline Extended
Reason: Not happy with the designs provided till now. Request all designers to once again look at the brief which is updated and submit maximum revisions. The pay is committed so we will select the best in any case. wish you all the best.

Target Market(s)

International - Current operations in the GCC, India, Srilanka

Industry/Entity Type

Construction Company

Font styles to use
Serif
Sans Serif

Requirements
Must have
• 1. A great front cover design - this may run to the back cover also
• 2. Inside page layout - to have a common theme but different styling as required
• 3. More of images and less of text - can use full page, half page or quarter page images.
• 4. Different styling and sizes for fonts for better effect.
Nice to have
• 1. A4 landscape is what we have in mind. The size can be slightly reduced so that the 80 page brochure can fit into an A4 envelope

```html
<!DOCTYPE html>
<html lang="en">
<head>
<meta charset="utf-8">
<title>Belvorant — Vision, Mission &amp; Corporate Social Responsibility</title>
<link rel="stylesheet" href="https://fonts.googleapis.com/css2?family=Tinos:wght@400;700&display=swap">
<style>
  :root {
    --backdrop: #a9a9ae;
    --paper: #ffffff;
    --paper-shade: #f1f1f2;
    --gold: #b09a58;
    --gold-dark: #8f7b3f;
    --green: #3e7a3a;
    --ink: #2b2b2b;
    --box-grey: #e6e6e7;
    --slate: #4a4a4c;
    --slate-deep: #333335;
    --slate-light: #6f6f72;
    --sky: #cfe0ee;
    --steel: #8a7a68;
    --white: #ffffff;
  }
  * { box-sizing: border-box; margin: 0; padding: 0; }
  html, body { width: 1200px; height: 900px; overflow: hidden; }
  body {
    background: var(--backdrop);
    font-family: "Tinos", "Times New Roman", serif;
    color: var(--ink);
  }
  .spread {
    position: absolute;
    left: 140px; top: 120px;
    width: 920px; height: 660px;
    display: flex;
  }
  .page {
    position: relative;
    width: 460px; height: 660px;
    overflow: hidden;
  }
  /* Left page */
  .page--left {
    background: linear-gradient(90deg, var(--paper) 0%, var(--paper) 88%, var(--paper-shade) 100%);
  }
  .hero-art { position: absolute; left: 0; top: 0; width: 460px; height: 300px; }
  .brand-mark {
    position: absolute;
    display: flex; align-items: center; gap: 7px;
    font-family: "Tinos", "Times New Roman", serif;
    font-weight: 700;
  }
  .brand-mark .dot { border-radius: 50%; background: var(--green); }
  .brand-mark--top { right: 26px; top: 26px; font-size: 24px; color: var(--green); }
  .brand-mark--top .dot { width: 12px; height: 12px; }

  .statement { position: absolute; left: 34px; right: 30px; }
  .statement--vision { top: 330px; }
  .statement--mission { top: 455px; }
  .statement h2 {
    font-size: 19px; font-weight: 700; text-align: center;
    margin-bottom: 10px; color: var(--ink);
  }
  .statement p {
    background: var(--box-grey);
    padding: 10px 12px;
    font-size: 11.5px; line-height: 1.45;
    color: #3a3a3a;
  }

  /* Right page */
  .page--right {
    background: linear-gradient(180deg, var(--slate-light) 0%, var(--slate) 45%, var(--slate-deep) 100%);
    color: var(--white);
  }
  .desk-photo {
    position: absolute; left: 0; top: 0; width: 460px; height: 230px;
    background: linear-gradient(180deg, #d8d2c8 0%, #a8a39c 55%, var(--slate-light) 100%);
  }
  .csr { position: absolute; left: 42px; right: 36px; top: 240px; }
  .csr h2 {
    font-size: 22px; font-weight: 700; text-align: center;
    margin-bottom: 14px; color: var(--white);
  }
  .csr p {
    font-size: 11px; line-height: 1.55; text-align: justify;
    color: #e4e4e4;
  }
  .brand-mark--bottom { right: 40px; bottom: 150px; font-size: 24px; color: var(--gold); }
  .brand-mark--bottom .dot { width: 12px; height: 12px; background: var(--gold); }
  .gutter {
    position: absolute; left: 450px; top: 0; width: 20px; height: 660px;
    background: linear-gradient(90deg, rgba(0,0,0,0) 0%, rgba(0,0,0,0.12) 50%, rgba(0,0,0,0) 100%);
    pointer-events: none;
  }
</style>
</head>
<body>
  <main class="spread">
    <section class="page page--left">
      <svg class="hero-art" viewBox="0 0 460 300" aria-hidden="false">
        <defs>
          <linearGradient id="siteTone" x1="0" y1="0" x2="0" y2="1">
            <stop offset="0" stop-color="var(--sky)"/>
            <stop offset="0.45" stop-color="#b9b0a2"/>
            <stop offset="1" stop-color="var(--steel)"/>
          </linearGradient>
        </defs>
        <path d="M0 40 L460 20 L460 210 Q300 250 0 300 Z" fill="url(#siteTone)" role="img" aria-label="Photo of a multi-storey building under construction with a tower crane"/>
        <path d="M0 0 L260 0 L0 90 Z" fill="var(--gold)"/>
        <path d="M260 0 L460 0 L460 20 L0 90 Z" fill="var(--paper)"/>
      </svg>
      <div class="brand-mark brand-mark--top"><span class="dot"></span>Belvorant</div>

      <article class="statement statement--vision">
        <h2>Vision</h2>
        <p>Belvorant aspires for a leading national and regional market position by delivering world class engineering, construction, and upholding top tier quality standards in the ecosystem of growth.</p>
      </article>

      <article class="statement statement--mission">
        <h2>Mission</h2>
        <p>We are committed to building long-term relationships based on integrity, performance, value, and client satisfaction. Delivering quality services and building long-term relationships based on integrity, performance, value, and client satisfaction.</p>
      </article>
    </section>

    <section class="page page--right">
      <div class="desk-photo" role="img" aria-label="Photo of an engineer's hands sketching plans at a desk"></div>
      <article class="csr">
        <h2>Corporate Social Responsibility</h2>
        <p>Belvorant Contracting believes that lasting growth depends on the communities we serve. We support local education, safe working conditions, and training programs for young engineers across every region. Our teams take part in environmental initiatives, reduce waste on site, and choose responsible suppliers. Through partnerships with schools, hospitals, and charities, we aim to leave each project stronger than we found it and to build trust with our neighbours.</p>
      </article>
      <div class="brand-mark brand-mark--bottom"><span class="dot"></span>Belvorant</div>
    </section>
    <div class="gutter"></div>
  </main>
</body>
</html>
```